Established food business needs a new name card design

Refer to attached current name card. Would like a new professional look design with only the company name and logo without any pictures. Would like green and yellow to be included.
To include:
My name "IBRAHIM SUKRI" and hand phone number "87260413".
To delete "
"Along Brackendale Ave 8" and
"www.nur-tiwas.com.sg"
To change email to:
"tkr27@velmorix.com.sg"

```html
<!DOCTYPE html>
<html lang="en">
<head>
<meta charset="utf-8">
<title>Nur-Tiwas Name Card</title>
<link href="https://fonts.googleapis.com/css2?family=Montserrat:wght@400;500;700&display=swap" rel="stylesheet">
<style>
  :root {
    --green: #114432;
    --yellow: #f2cf1b;
    --white: #ffffff;
    --paper: #f6f6f6;
    --ink: #222222;
    --bg: #d4d6d8;
  }
  * { margin: 0; padding: 0; box-sizing: border-box; }
  html, body { width: 1200px; height: 800px; overflow: hidden; }
  body {
    background: var(--bg);
    font-family: "Montserrat", sans-serif;
    position: relative;
  }
  .card {
    position: absolute;
    width: 600px;
    height: 343px;
    overflow: hidden;
    box-shadow: 0 6px 16px rgba(0,0,0,0.18);
  }
  .card-back {
    left: 450px;
    top: 40px;
    background: var(--green);
  }
  .card-front {
    left: 150px;
    top: 417px;
    background: var(--paper);
  }
  .brand {
    position: absolute;
    display: flex;
    align-items: center;
    gap: 14px;
    color: var(--yellow);
    font-weight: 700;
    letter-spacing: 1px;
  }
  .brand-dot {
    border-radius: 50%;
    border: 4px solid var(--yellow);
  }
  .card-back .brand { left: 150px; top: 140px; font-size: 40px; }
  .card-back .brand-dot { width: 52px; height: 52px; }
  .back-ring {
    position: absolute;
    right: -40px;
    top: 60px;
    width: 300px;
    height: 300px;
    border-radius: 50%;
    border: 10px solid rgba(255,255,255,0.06);
  }
  .front-wave { position: absolute; left: 0; top: 0; width: 600px; height: 343px; }
  .card-front .brand { left: 32px; top: 38px; font-size: 32px; }
  .card-front .brand-dot { width: 42px; height: 42px; }
  .contact {
    position: absolute;
    right: 40px;
    top: 178px;
    text-align: right;
    color: var(--ink);
  }
  .contact-name {
    color: var(--green);
    font-weight: 700;
    font-size: 20px;
    letter-spacing: 0.5px;
    margin-bottom: 20px;
  }
  .contact-line {
    display: flex;
    justify-content: flex-end;
    align-items: center;
    gap: 8px;
    font-size: 14px;
    line-height: 22px;
  }
  .contact-line svg { width: 15px; height: 15px; fill: none; stroke: var(--green); stroke-width: 2; }
  .address {
    position: absolute;
    left: 32px;
    right: 40px;
    bottom: 28px;
    text-align: right;
    font-size: 13.5px;
    color: var(--ink);
  }
</style>
</head>
<body>
  <section class="card card-back">
    <div class="back-ring"></div>
    <div class="brand"><span class="brand-dot"></span><span class="brand-name">NUR-TIWAS</span></div>
  </section>

  <section class="card card-front">
    <svg class="front-wave" viewBox="0 0 600 343" preserveAspectRatio="none">
      <path d="M0 0 H600 V125 C470 170 350 150 230 120 C140 100 60 105 0 125 Z" fill="var(--green)"/>
      <path d="M0 125 C60 105 140 100 230 120 C350 150 470 170 600 125 V148 C470 195 350 178 230 146 C140 125 60 125 0 150 Z" fill="var(--yellow)"/>
    </svg>
    <div class="brand"><span class="brand-dot"></span><span class="brand-name">NUR-TIWAS</span></div>
    <div class="contact">
      <p class="contact-name">IBRAHIM SUKRI</p>
      <p class="contact-line">87260413
        <svg viewBox="0 0 24 24"><path d="M5 3h4l2 5-3 2a12 12 0 0 0 6 6l2-3 5 2v4a2 2 0 0 1-2 2A17 17 0 0 1 3 5a2 2 0 0 1 2-2z"/></svg>
      </p>
      <p class="contact-line">tkr27@velmorix.com.sg
        <svg viewBox="0 0 24 24"><rect x="3" y="5" width="18" height="14"/><path d="M3 5l9 7 9-7"/></svg>
      </p>
    </div>
    <p class="address">18 Kelvadon Industrial, Estate Road 6 # 02-14, Singapore 748163</p>
  </section>
</body>
</html>
```